Create modern and sleek business card for luxury real estate company

We're a "boutique" real estate office looking for a design that gets across a highly modern luxury brand. Blacks and whites are probably the best colors unless we try a silver foil for the logo. I've attached a version of our current logo here. I'd like to swap out the current font on there with Gotham Light Regular.

I'm looking to have one side of the card have the logo with the space for our agents info on the other side.

Target Market(s)

Young professionals in a "luxury" headspace

Industry/Entity Type

Real estate

Contact Information for Business Card

A place for agent name, cell number, website. The slogan "Quietly Redefining Real Estate".

Font styles to use
Other font styles liked:
• Gotham Regular

Colors

Designer to choose only greyscale colors for use in the design.

Requirements
Must have
• Matte black as the background color. Clean lines and use of contrast. A specific design aspect that will use silver foil.
Nice to have
• Up in the air on integrating a QR code
Should not have
• Any houses or other real estate related design (ex: a clip art house)

```html
<!DOCTYPE html>
<html lang="en">
<head>
<meta charset="utf-8">
<title>Solace Realty – Business Card</title>
<link href="https://fonts.googleapis.com/css2?family=Montserrat:wght@300;400;600&display=swap" rel="stylesheet">
<style>
  :root {
    --page: #ffffff;
    --card: #000000;
    --ink: #f2f0ea;
    --silver: #d9d6cc;
    --rule: #3a3a3a;
    --edge: #2a2626;
  }
  html, body {
    margin: 0;
    padding: 0;
    width: 1200px;
    height: 1200px;
    overflow: hidden;
    background: var(--page);
    font-family: "Montserrat", Arial, sans-serif;
  }
  .card {
    position: absolute;
    left: 319px;
    width: 561px;
    height: 320px;
    background: var(--card);
    border: 1px solid var(--edge);
    box-shadow: 4px 6px 10px rgba(0,0,0,0.18);
    box-sizing: border-box;
    overflow: hidden;
  }
  .card--front { top: 237px; }
  .card--back  { top: 627px; }

  .mark-ring {
    position: absolute;
    border: 1px solid var(--silver);
    border-radius: 50%;
    box-sizing: border-box;
    display: flex;
    align-items: center;
    justify-content: center;
    color: var(--silver);
    font-weight: 300;
  }
  .divider {
    position: absolute;
    width: 1px;
    background: #6a6a6a;
  }

  /* Front */
  .card--front .mark-ring { left: 139px; top: 121px; width: 78px; height: 78px; }
  .card--front .divider { left: 235px; top: 122px; height: 77px; }
  .brand-name {
    position: absolute;
    left: 255px;
    top: 126px;
    margin: 0;
    color: var(--ink);
    font-weight: 300;
    font-size: 35px;
    line-height: 33px;
    letter-spacing: 3px;
  }

  /* Back */
  .card--back .mark-ring { left: 122px; top: 100px; width: 116px; height: 116px; font-size: 14px; letter-spacing: 3px; }
  .card--back .divider { left: 266px; top: 98px; height: 120px; }
  .agent {
    position: absolute;
    left: 294px;
    top: 110px;
    color: var(--ink);
  }
  .agent-name {
    margin: 0;
    font-weight: 300;
    font-size: 22px;
    line-height: 26px;
    letter-spacing: 0.5px;
  }
  .agent-title {
    margin: 2px 0 0;
    font-weight: 300;
    font-size: 14px;
    line-height: 16px;
  }
  .contact {
    list-style: none;
    margin: 15px 0 0 5px;
    padding: 0;
    font-size: 13px;
    line-height: 16.5px;
    font-weight: 300;
    white-space: nowrap;
  }
  .contact b {
    display: inline-block;
    width: 21px;
    font-size: 12px;
    font-weight: 600;
  }
  .slogan-band {
    position: absolute;
    left: 0;
    right: 0;
    top: 265px;
    height: 26px;
    border-top: 1px solid var(--rule);
    border-bottom: 1px solid var(--rule);
    display: flex;
    align-items: center;
    justify-content: center;
    color: var(--ink);
    font-size: 12.5px;
    font-weight: 400;
    letter-spacing: 2.4px;
    white-space: nowrap;
  }
</style>
</head>
<body>
  <section class="card card--front">
    <div class="mark-ring"></div>
    <div class="divider"></div>
    <h1 class="brand-name">SOLACE<br>REALTY</h1>
  </section>

  <section class="card card--back">
    <div class="mark-ring">SOLACE</div>
    <div class="divider"></div>
    <div class="agent">
      <p class="agent-name">AGENT NAME</p>
      <p class="agent-title">Title</p>
      <ul class="contact">
        <li><b>C:</b>000 218 7390</li>
        <li><b>E:</b>info@solacerealty.com</li>
        <li><b>W:</b>www.solacerealty.com</li>
      </ul>
    </div>
    <div class="slogan-band">"Quietly Redefining Real Estate".</div>
  </section>
</body>
</html>
```